business cards and stationary for equipment mfg.
Brunwick Incorporated
business cards and stationary for equipment mfg. - Manufacturing
Creative Brief
Professional
Dennis Moray
President
418 Pell Creek Road Alderton, Iowa 47193
dennismoray@brunwickinc.example
www.brunwickinc.example
Business card should reflect the logo supplied but we will welcome the artest interpretation.

```html
<!DOCTYPE html>
<html lang="en">
<head>
<meta charset="utf-8">
<title>Brunwick Incorporated — Stationery</title>
<link href="https://fonts.googleapis.com/css2?family=Open+Sans:wght@400;600;700&family=Oswald:wght@500&display=swap" rel="stylesheet">
<style>
  :root{
    --stage:#2b2624;
    --paper:#f4f4f5;
    --paper-edge:#e2e3e6;
    --ink:#3a3d44;
    --ink-soft:#7b8089;
    --navy:#1b3f7a;
    --brand-blue:#1a7fd0;
    --folder-deep:#0d3f86;
    --folder-mid:#1670c8;
    --folder-glow:#2ec4ea;
    --white:#ffffff;
  }
  *{box-sizing:border-box;margin:0;padding:0}
  html,body{width:1200px;height:915px;overflow:hidden}
  body{background:var(--stage);font-family:"Open Sans",Arial,sans-serif;color:var(--ink);position:relative}

  .sheet{position:absolute;box-shadow:0 10px 26px rgba(0,0,0,.45)}

  .brand{display:flex;align-items:center;gap:8px}
  .brand__dot{border-radius:50%;background:var(--brand-blue);flex:none}
  .brand__name{font-weight:700;letter-spacing:.04em;text-transform:uppercase;color:var(--navy);white-space:nowrap}

  .letterhead{left:40px;top:40px;width:380px;height:492px;background:var(--paper);padding:34px 36px}
  .letterhead__top{display:flex;justify-content:space-between;align-items:flex-start}
  .letterhead .brand{margin-top:26px}
  .letterhead .brand__dot{width:26px;height:26px}
  .letterhead .brand__name{font-size:15px}
  .contact{list-style:none;font-size:6.5px;color:var(--ink-soft);line-height:1.35}
  .contact li{display:flex;align-items:flex-start;gap:5px;margin-bottom:2px}
  .contact svg{width:7px;height:7px;flex:none;margin-top:1px;fill:var(--brand-blue)}
  .letter{margin-top:70px;font-size:7.4px;line-height:1.6;color:var(--ink)}
  .letter__greeting{font-size:9px;margin-bottom:14px}
  .letter p{margin-bottom:10px;text-align:justify}
  .letter__sign{margin-top:26px;font-size:9.5px}
  .letter__role{font-size:6.5px;color:var(--ink-soft);margin-top:2px}

  .folder{left:460px;top:40px;width:380px;height:492px;
    background:radial-gradient(circle at 50% 52%,var(--folder-glow) 0%,var(--folder-mid) 42%,var(--folder-deep) 100%);
    display:flex;align-items:center;justify-content:center}
  .folder .brand__dot{width:34px;height:34px;background:var(--white)}
  .folder .brand__name{font-size:26px;color:var(--white)}

  .envelope{left:40px;top:572px;width:580px;height:250px;background:var(--paper);padding:24px 28px}
  .envelope__head{display:flex;flex-direction:column;align-items:flex-end;gap:6px}
  .envelope .brand__dot{width:22px;height:22px}
  .envelope .brand__name{font-size:15px}
  .envelope__address{font-size:7.5px;letter-spacing:.12em;color:var(--ink)}

  .card{width:290px;height:166px;left:880px}
  .card--front{top:40px;background:linear-gradient(135deg,var(--brand-blue) 0%,var(--folder-deep) 100%);color:var(--white);padding:18px 20px}
  .card__name{font-family:"Oswald","Arial Narrow",sans-serif;font-weight:500;font-size:15px;letter-spacing:.03em;text-transform:uppercase}
  .card__role{font-size:6.5px;opacity:.85;margin-bottom:18px}
  .card--front .contact{color:var(--white);font-size:6.8px}
  .card--front .contact svg{fill:var(--white)}
  .card--back{top:236px;background:var(--paper);padding:18px 20px;display:flex;flex-direction:column;justify-content:space-between}
  .card--back .brand__dot{width:14px;height:14px}
  .card--back .brand__name{font-size:10px}
  .card__web{font-size:6.5px;letter-spacing:.14em;color:var(--ink-soft);align-self:center}
</style>
</head>
<body>

<svg width="0" height="0" style="position:absolute" aria-hidden="true">
  <symbol id="icon-pin" viewBox="0 0 10 10"><path d="M5 0a3.5 3.5 0 0 0-3.5 3.5C1.5 6 5 10 5 10s3.5-4 3.5-6.5A3.5 3.5 0 0 0 5 0zm0 5a1.5 1.5 0 1 1 0-3 1.5 1.5 0 0 1 0 3z"/></symbol>
  <symbol id="icon-phone" viewBox="0 0 10 10"><path d="M2.2 0.5 3.8 2.3 3 3.6c.6 1.3 1.8 2.5 3.3 3.3l1.3-.8 1.8 1.6-1 1.6C4.8 9.2.8 5.2.5 1.5z"/></symbol>
  <symbol id="icon-fax" viewBox="0 0 10 10"><path d="M2.5 0h5v3h-5zM0 3.5h10V8H8v2H2V8H0zm3 3.5v2h4V7z"/></symbol>
  <symbol id="icon-mail" viewBox="0 0 10 10"><path d="M0 2h10v6H0zm1 1v.4L5 6l4-2.6V3z"/></symbol>
  <symbol id="icon-web" viewBox="0 0 10 10"><circle cx="5" cy="5" r="4.5" fill="none" stroke="currentColor"/><path d="M0.5 5h9M5 .5c-2 2.5-2 6.5 0 9M5 .5c2 2.5 2 6.5 0 9" fill="none" stroke="currentColor" stroke-width=".8"/></symbol>
</svg>

<section class="sheet letterhead" aria-label="Letterhead">
  <header class="letterhead__top">
    <div class="brand"><span class="brand__dot"></span><span class="brand__name">Brunwick Inc.</span></div>
    <ul class="contact">
      <li><svg><use href="#icon-pin"/></svg><span>418 Pell Creek Road<br>Alderton, Iowa 47193</span></li>
      <li><svg><use href="#icon-phone"/></svg><span>555-014-2281</span></li>
      <li><svg><use href="#icon-fax"/></svg><span>555-014-2290</span></li>
      <li><svg style="color:var(--brand-blue)"><use href="#icon-mail"/></svg><span>dennismoray@brunwickinc.example</span></li>
      <li><svg style="color:var(--brand-blue)"><use href="#icon-web"/></svg><span>www.brunwickinc.example</span></li>
    </ul>
  </header>
  <div class="letter">
    <p class="letter__greeting">Dear Mr. Alder,</p>
    <p>Lorem ipsum dolor sit amet, consectetur adipiscing elit. Donec orci purus, luctus vitae dignissim eu, iaculis sed purus. Vivamus faucibus, ipsum nec aliquet viverra, leo mauris condimentum ligula, sit amet sagittis enim ligula quis arcu. Nam egestas tortor id nisi porttitor mattis. In tortor ante, ultricies in suscipit a, tempus non massa. Vivamus et auctor mi. Fusce vel massa nulla. Phasellus nec eros mauris, et scelerisque orci. Donec malesuada orci vitae nulla accumsan porta a id massa. Quisque accumsan iaculis magna sit amet fringilla. Maecenas consequat, magna eget tincidunt semper, odio nibh rutrum mi, id feugiat ante nisi eu risus. Vestibulum nunc orci, rhoncus a placerat in, ultricies in mi. Cras mattis varius eros, vel fringilla nisi suscipit eget.</p>
    <p>Quisque scelerisque sagittis nulla at porttitor. Mauris a justo et tellus interdum tristique. Sed id augue vitae urna euismod commodo aliquet a quam. Pellentesque arcu velit, cursus et malesuada ut, consequat et diam. Nullam erat sem, rhoncus id ullamcorper vitae, rhoncus et arcu. In ultricies ultricies nulla, ut rutrum nisi iaculis at. Donec eu magna a metus ornare faucibus. Fusce aliquet faucibus ultricies. Morbi semper, est id tincidunt gravida, sem arcu adipiscing lacus, ac bibendum nulla leo eu purus. Quisque nec diam sed risus consectetur accumsan quis nibh. Vestibulum id purus lorem.</p>
    <p class="letter__sign">Dennis Moray</p>
    <p class="letter__role">President</p>
  </div>
</section>

<section class="sheet folder" aria-label="Presentation folder">
  <div class="brand"><span class="brand__dot"></span><span class="brand__name">Brunwick Inc.</span></div>
</section>

<section class="sheet envelope" aria-label="Envelope">
  <div class="envelope__head">
    <div class="brand"><span class="brand__dot"></span><span class="brand__name">Brunwick Inc.</span></div>
    <p class="envelope__address">418 Pell Creek Road Alderton, Iowa 47193</p>
  </div>
</section>

<section class="sheet card card--front" aria-label="Business card front">
  <p class="card__name">Dennis Moray</p>
  <p class="card__role">President</p>
  <ul class="contact">
    <li><svg><use href="#icon-pin"/></svg><span>418 Pell Creek Road<br>Alderton, Iowa 47193</span></li>
    <li><svg><use href="#icon-phone"/></svg><span>555-014-2281</span></li>
    <li><svg><use href="#icon-fax"/></svg><span>555-014-2290</span></li>
    <li><svg><use href="#icon-mail"/></svg><span>dennismoray@brunwickinc.example</span></li>
    <li><svg style="color:var(--white)"><use href="#icon-web"/></svg><span>www.brunwickinc.example</span></li>
  </ul>
</section>

<section class="sheet card card--back" aria-label="Business card back">
  <div class="brand"><span class="brand__dot"></span><span class="brand__name">Brunwick Inc.</span></div>
  <p class="card__web">www.brunwickinc.example</p>
</section>

</body>
</html>
```